Update our business cards to match our awesome new website

Need a new design for company business cards. We have recently revamped our website and would like our business cards to get a refresh too. I've uploaded the company artwork, logo, as well as the Branding Deck to better understand the look & feel of our brand. Please visit the website at bellcrestholdingsoh.com.

Industry/Entity Type

Real Estate

Contact Information for Business Card

must use the colors outlined in the Branding Deck uploaded to the site, or the colors of our logo.

Font styles to use
Other font styles liked:
• Calibri

Requirements
Must have
• Required items: Name, title, company logo, address: 217 Fennimore Ave. Suite 300, Lakeport, OH 44093, email address: glen@bellcrestholdingsOH.com, company phone 800-555-0172, cell: 216-555-0148
Nice to have
• a more simple design. not complicated
Should not have
• cartoonish characters, or whimsical writing or artwork, stay within our branding colors

```html
<!DOCTYPE html>
<html lang="en">
<head>
<meta charset="utf-8">
<title>Bellcrest Holdings – Business Cards</title>
<link href="https://fonts.googleapis.com/css2?family=Carlito:wght@400;700&display=swap" rel="stylesheet">
<style>
  :root {
    --bg: #3b3b3d;
    --card-white: #ffffff;
    --brand-green: #77b743;
    --brand-green-dark: #4f9a3e;
    --ink: #2b2b2b;
    --logo-ink: #1c1c1c;
  }
  * { margin: 0; padding: 0; box-sizing: border-box; }
  html, body {
    width: 1200px;
    height: 1059px;
    overflow: hidden;
    background: var(--bg);
    font-family: "Carlito", "Calibri", sans-serif;
  }
  .canvas { position: relative; width: 1200px; height: 1059px; }

  .card {
    position: absolute;
    border-radius: 18px;
    overflow: hidden;
  }
  .card-front {
    left: 256px; top: 100px; width: 688px; height: 391px;
    background: var(--card-white);
  }
  .card-back {
    left: 253px; top: 537px; width: 694px; height: 394px;
    background: var(--brand-green);
  }

  .accent-bar {
    position: absolute; left: 0; top: 110px;
    width: 13px; height: 37px;
    background: var(--brand-green);
  }
  .holder { position: absolute; left: 29px; top: 104px; }
  .holder-name {
    font-size: 24px; font-weight: 700; line-height: 1;
    color: var(--brand-green); letter-spacing: 0.2px;
  }
  .holder-title {
    margin-top: 5px;
    font-size: 17px; color: var(--ink); line-height: 1;
  }

  .address {
    position: absolute; left: 29px; top: 184px;
    font-size: 15.5px; line-height: 20px; color: var(--ink);
  }
  .contacts {
    position: absolute; left: 29px; top: 233px;
    list-style: none;
    font-size: 15.5px; color: var(--ink);
  }
  .contacts li {
    display: flex; align-items: center; gap: 6px;
    height: 19px;
  }
  .contacts svg { width: 12px; height: 12px; flex: none; }
  .web-domain { color: var(--brand-green-dark); }

  .front-wordmark {
    position: absolute; right: 30px; top: 124px;
    font-size: 28px; font-weight: 400; color: var(--logo-ink);
    letter-spacing: 0.5px; line-height: 1;
  }

  .wave { position: absolute; left: 0; top: 0; width: 688px; height: 391px; }

  .back-wordmark {
    position: absolute; left: 0; right: 0; top: 222px;
    text-align: center;
    font-size: 46px; font-weight: 400; color: var(--card-white);
    letter-spacing: 1px; line-height: 1;
  }
</style>
</head>
<body>
<main class="canvas">

  <section class="card card-front" aria-label="Business card front">
    <div class="accent-bar"></div>
    <div class="holder">
      <h1 class="holder-name">GLEN PORTER</h1>
      <p class="holder-title">Owner</p>
    </div>

    <p class="address">217 Fennimore Ave. Suite<br>300 Lakeport, OH 44093</p>

    <ul class="contacts">
      <li>
        <svg viewBox="0 0 12 12" aria-hidden="true"><path d="M2.5 1l2 2.2-1 1.2c.6 1.4 1.7 2.5 3.1 3.1l1.2-1 2.2 2-1 1.5C5.5 10 2 6.5 1 2z" fill="var(--brand-green)"/></svg>
        800-555-0172
      </li>
      <li>
        <svg viewBox="0 0 12 12" aria-hidden="true"><path d="M1 5c2-3 8-3 10 0l-1.5 1L8 5V4H4v1L2.5 6zM3 6h6l1 4H2z" fill="var(--brand-green)"/></svg>
        216-555-0148
      </li>
      <li>
        <svg viewBox="0 0 12 12" aria-hidden="true"><rect x="1" y="2.5" width="10" height="7" fill="var(--brand-green)"/><path d="M1 2.5l5 4 5-4M1 9.5l3.8-3.5M11 9.5L7.2 6" stroke="#fff" stroke-width="0.9" fill="none"/></svg>
        glen@bellcrestholdingsOH.com
      </li>
      <li>
        <svg viewBox="0 0 12 12" aria-hidden="true"><circle cx="6" cy="6" r="5.2" fill="var(--brand-green)"/><path d="M3 4c1 0 2 1 1.5 2S5 8 4.5 9.5M7.5 2c0 1.5 1.5 1.5 2 3" stroke="#fff" stroke-width="1" fill="none"/></svg>
        <span>www.<span class="web-domain">bellcrestholdingsoh</span>.com</span>
      </li>
    </ul>

    <p class="front-wordmark">Bellcrest Holdings</p>

    <svg class="wave" viewBox="0 0 688 391" aria-hidden="true">
      <path d="M0 332 C90 365 170 376 260 370 C420 356 540 330 688 337 L688 350 C560 340 430 364 260 375 C160 382 80 370 0 345 Z" fill="var(--brand-green-dark)"/>
      <path d="M0 346 C90 372 170 382 260 376 C430 362 560 341 688 352" stroke="#fff" stroke-width="1.6" fill="none"/>
      <path d="M200 375 C380 360 520 334 688 345 L688 391 L0 391 L0 350 C70 372 140 378 200 375 Z" fill="var(--brand-green)"/>
    </svg>
  </section>

  <section class="card card-back" aria-label="Business card back">
    <p class="back-wordmark">Bellcrest Holdings</p>
  </section>

</main>
</body>
</html>
```